Bref créative
vostelmira #20
Real Estate Investors
Professional
Dale Quistorff
President
8316 Willowmere Rd, Ste. 217 (#492)
Calderidge, TX 75218
dquistorff@mailvessa.com
Please make 100 cards in the name of Dale Quistorff and the other 100 cards in the name of: Colette Quistorff, Title: Program Director, Address: Same, Phone: Same, Cell: 214 637-2940, E-mail: colette.quistorff@mailvessa.com.
Keep in mind we will request an update on this card in a later date with the following: Website Address, Fax #, and Toll Free #.

```html
<!DOCTYPE html>
<html lang="en">
<head>
<meta charset="utf-8">
<title>Tolvanex — Business Card</title>
<link href="https://fonts.googleapis.com/css2?family=Cinzel:wght@400;600&display=swap" rel="stylesheet">
<style>
  :root {
    --page-bg: #e9e6e2;
    --card-red: #e2353b;
    --card-red-dark: #c8242c;
    --card-black: #0c0c0c;
    --edge-grey: #8d8d8d;
    --text-dark: #1a1a1a;
    --text-light: #ffffff;
    --brand-red: #e2353b;
  }
  * { margin: 0; padding: 0; box-sizing: border-box; }
  html, body {
    width: 1200px;
    height: 914px;
    overflow: hidden;
    background: var(--page-bg);
  }
  .canvas {
    position: relative;
    width: 1200px;
    height: 914px;
  }
  .business-card {
    position: absolute;
    left: 75px;
    top: 157px;
    width: 1050px;
    height: 600px;
    overflow: hidden;
    background: linear-gradient(135deg, var(--card-red) 0%, var(--card-red-dark) 100%);
    box-shadow: 0 18px 40px rgba(0,0,0,0.25);
    font-family: "Cinzel", "Times New Roman", serif;
  }
  .card-shape {
    position: absolute;
    inset: 0;
    width: 100%;
    height: 100%;
  }
  .holder {
    position: absolute;
    left: 60px;
    top: 44px;
    color: var(--text-dark);
  }
  .holder-name {
    font-size: 30px;
    font-weight: 600;
    letter-spacing: 0.5px;
  }
  .holder-title {
    font-size: 17px;
    letter-spacing: 1px;
    margin-top: 2px;
  }
  .contact-list {
    position: absolute;
    left: 60px;
    top: 280px;
    list-style: none;
    color: var(--text-light);
    font-size: 16px;
    letter-spacing: 0.6px;
    text-transform: uppercase;
  }
  .contact-item {
    display: flex;
    align-items: center;
    height: 30px;
    white-space: nowrap;
  }
  .contact-icon {
    width: 22px;
    height: 22px;
    margin-right: 12px;
    flex: none;
  }
  .contact-icon.is-blank { visibility: hidden; }
  .brand {
    position: absolute;
    left: 640px;
    top: 278px;
    width: 360px;
    text-align: center;
    color: var(--brand-red);
    font-size: 58px;
    font-weight: 600;
    letter-spacing: 2px;
  }
</style>
</head>
<body>
<main class="canvas">
  <article class="business-card">
    <svg class="card-shape" viewBox="0 0 1050 600" aria-hidden="true">
      <path d="M652,0 C572,8 552,120 514,260 C482,380 452,560 392,600 L1050,600 L1050,0 Z" fill="var(--edge-grey)"/>
      <path d="M664,0 C584,8 564,120 526,260 C494,380 464,560 404,600 L1050,600 L1050,0 Z" fill="var(--card-black)"/>
    </svg>

    <header class="holder">
      <h1 class="holder-name">Dale Quistorff</h1>
      <p class="holder-title">President</p>
    </header>

    <ul class="contact-list">
      <li class="contact-item">
        <svg class="contact-icon" viewBox="0 0 24 24" aria-hidden="true"><circle cx="12" cy="12" r="11" fill="#fff"/><path d="M12 5.5a4 4 0 0 0-4 4c0 3 4 8 4 8s4-5 4-8a4 4 0 0 0-4-4zm0 5.5a1.5 1.5 0 1 1 0-3 1.5 1.5 0 0 1 0 3z" fill="var(--card-red)"/></svg>
        <span>8316 Willowmere Rd, Ste. 217</span>
      </li>
      <li class="contact-item">
        <svg class="contact-icon is-blank" viewBox="0 0 24 24" aria-hidden="true"></svg>
        <span>#492 Calderidge, TX 75218</span>
      </li>
      <li class="contact-item">
        <svg class="contact-icon" viewBox="0 0 24 24" aria-hidden="true"><circle cx="12" cy="12" r="11" fill="#fff"/><path d="M8.5 6.5l2 2.2-1.2 1.6c.8 1.7 2 2.9 3.7 3.7l1.6-1.2 2.2 2-1.3 1.8c-4.5-.6-8.2-4.3-8.8-8.8z" fill="var(--card-red)"/></svg>
        <span>214 508-7716</span>
      </li>
      <li class="contact-item">
        <svg class="contact-icon" viewBox="0 0 24 24" aria-hidden="true"><circle cx="12" cy="12" r="11" fill="#fff"/><rect x="6" y="8" width="12" height="8.5" rx="1" fill="var(--card-red)"/><path d="M6.5 8.5l5.5 4.2 5.5-4.2" fill="none" stroke="#fff" stroke-width="1.2"/></svg>
        <span>dquistorff@mailvessa.com</span>
      </li>
    </ul>

    <p class="brand">Tolvanex</p>
  </article>
</main>
</body>
</html>
```